Boarding Pass for Tour Company

We need an A6 sized boarding pass desinged for our tour company.

Colours to follow company logo. Image background with white text on top.

Require a strip at the bottom with text on top. This will be a group indicator colour. Can use purple for design.

Font styles to use
Sans Serif

Colors
0054AA
0677BA
7BADD7
CADEEF
E8F1F8

```html
<!DOCTYPE html>
<html lang="en">
<head>
<meta charset="UTF-8">
<title>Skyward Drift Boarding Pass</title>
<link href="https://fonts.googleapis.com/css2?family=Orbitron:wght@500;700;900&display=swap" rel="stylesheet">
<style>
  :root {
    --backdrop: #dcdcdc;
    --brand-deep: #0054aa;
    --brand-blue: #0677ba;
    --brand-sky: #29a6e0;
    --brand-light: #7badd7;
    --brand-pale: #cadeef;
    --brand-mist: #e8f1f8;
    --ink: #000000;
    --paper: #ffffff;
    --group-purple: #9c27c6;
    --field-green: #6f7a2c;
    --field-gold: #b9a445;
  }
  * { margin: 0; padding: 0; box-sizing: border-box; }
  html, body {
    width: 1200px;
    height: 800px;
    overflow: hidden;
    background: var(--backdrop);
  }
  .pass {
    position: absolute;
    left: 392px;
    top: 118px;
    width: 404px;
    height: 564px;
    background: var(--paper);
    overflow: hidden;
    font-family: "Orbitron", sans-serif;
  }
  .pass__photo {
    position: absolute;
    left: 0; top: 0;
    width: 404px; height: 278px;
    background: linear-gradient(180deg,
      var(--brand-mist) 0%,
      var(--brand-pale) 45%,
      #efe2c8 66%,
      #8c8a4a 72%,
      var(--field-gold) 80%,
      var(--field-green) 100%);
  }
  .pass__brand {
    position: absolute;
    left: 168px;
    top: 64px;
    width: 200px;
    text-align: center;
    font-weight: 700;
    font-size: 20px;
    line-height: 1.2;
    color: var(--brand-sky);
  }
  .pass__banner {
    position: absolute;
    left: 0; top: 278px;
    width: 404px; height: 142px;
  }
  .pass__hashtag-band {
    position: absolute;
    left: 0; top: 392px;
    width: 404px; height: 86px;
    background: var(--ink);
  }
  .pass__title {
    position: absolute;
    left: 0; top: 292px;
    width: 404px;
    text-align: center;
    font-weight: 900;
    font-size: 52px;
    line-height: 54px;
    letter-spacing: 0.5px;
    color: var(--paper);
    -webkit-text-stroke: 1.5px var(--ink);
    text-shadow: 2px 3px 0 var(--ink);
  }
  .pass__hashtag {
    position: absolute;
    left: 0; top: 438px;
    width: 404px;
    text-align: center;
    font-weight: 500;
    font-size: 17px;
    letter-spacing: 0.5px;
    color: var(--paper);
  }
  .pass__group {
    position: absolute;
    left: 0; top: 478px;
    width: 404px; height: 86px;
    background: var(--group-purple);
    display: flex;
    align-items: center;
    justify-content: center;
  }
  .pass__pilot {
    font-weight: 500;
    font-size: 25px;
    letter-spacing: 1px;
    color: var(--paper);
  }
</style>
</head>
<body>
  <div class="pass">
    <div class="pass__photo" role="img" aria-label="Hot air balloons drifting over vineyards and gum trees at sunrise"></div>
    <div class="pass__brand">Skyward Drift</div>

    <svg class="pass__banner" width="404" height="142" viewBox="0 0 404 142" aria-hidden="true">
      <defs>
        <linearGradient id="bannerBlue" x1="0" y1="0" x2="0" y2="1">
          <stop offset="0" stop-color="#0a82c8"/>
          <stop offset="1" stop-color="#29a6e0"/>
        </linearGradient>
      </defs>
      <rect x="0" y="0" width="404" height="114" fill="url(#bannerBlue)"/>
      <polygon points="85,113 319,113 307,142 98,142" fill="#29a6e0"/>
    </svg>
    <div class="pass__hashtag-band"></div>
    <svg style="position:absolute;left:0;top:392px" width="404" height="30" viewBox="0 0 404 30" aria-hidden="true">
      <polygon points="85,0 319,0 307,28 98,28" fill="#29a6e0"/>
    </svg>

    <h1 class="pass__title">BOARDING<br>PASS</h1>
    <p class="pass__hashtag">#skywarddrift</p>

    <div class="pass__group">
      <p class="pass__pilot">PILOT: OWEN</p>
    </div>
  </div>
</body>
</html>
```